Advertising agency needs site design

You will be designing a clean (plenty of white space) and vivid (colorful) design that is for an advertising agency named Pixel Harbor. Their current web site is located at www.PixelHarbor.net. From there you can see their services and get a feel for the company as the site stands today.
The following are direct quotes from the client:
“I want a clean look with colors of the teal blue, deep yellow (in logo) and then a good energetic orange (deep orange - rich) should bring a good feel and enthusiasm.”
“The orange can be a nice accent color, not dominant.”
“Saw two other things I like - the website brightkitemedia.com was pretty cool. I liked how the top banner changed colors as you moved to different tabs. I am somewhat wanting the colors I mentioned - like the blue color we use can be lighter as long as it works with the logo. - love the loop leaves site. I want quirky, creative and clean look - fun feel but slightly sophisticated to work with the medical field.”
Pixel Harbor currently focuses on the following primary industries:
• Medical / Health Care – Currently the primary industry
• Retail Industry
• Automotive Industry
• Entertainment Industry
Primary Services
• Media Planning & Buying: Web, TV, Print, Radio
• Campaign monitoring and reporting
• Commercial Production: TV & Radio
• Strategic Planning
• Market Research
• Internet Marketing: Email, SEO, Web design / development
Primary Navigation will consist of the following:
• Home
• About Us
o History
o Principal Profile (sub nav)
o Sales Team & Partners
• Clients
• Services
• Testimonials
• Contact Us
They want the web site to act as a basis for future marketing collateral so the overall feel from the web site must be capable of translating to print and other collateral. I do not currently have a clean digital version of their logo however their logo is on the web site (pixelharbor.net)
Reason: Still awaiting feedback from client on designs. They should be back to us shortly.
Target Market(s)
larger companies that are purchasing air time on television and radio. Typically in the health care industry and others described above in brief.
Industry/Entity Type
Advertising

```html
<!DOCTYPE html>
<html lang="en">
<head>
<meta charset="utf-8">
<title>Pixel Harbor – Advertising Agency</title>
<link href="https://fonts.googleapis.com/css2?family=Arimo:wght@400;700&family=Tinos&display=swap" rel="stylesheet">
<style>
:root{
  --teal:#1d6f9a;
  --navy:#1a3f8f;
  --gold:#f0a81c;
  --orange-band:#e39a12;
  --orange-light:#f5b830;
  --green:#8cab22;
  --blue-box:#045985;
  --red-box:#b5090b;
  --ink:#333;
  --rust:#c0300a;
  --line:#bbb;
  --panel:#f2f2f2;
}
*{box-sizing:border-box;margin:0;padding:0}
html,body{width:1200px;height:999px;overflow:hidden}
body{font-family:"Arimo",sans-serif;color:var(--ink);background:#fff;position:relative}
.abs{position:absolute}
.header{left:0;top:0;width:1200px;height:90px;background:linear-gradient(#eaeaea,#f1f1f1)}
.brand{color:var(--teal);font-size:30px;font-weight:400;white-space:nowrap}
.header .brand{left:168px;top:27px}
.phones{right:110px;top:20px;color:var(--navy);font-size:21px;line-height:28px}
.nav{left:0;top:89px;width:1200px;height:31px;background:linear-gradient(#fff,#eee);border-top:1px solid var(--gold);display:flex;padding-left:231px}
.nav a{font-size:12px;color:var(--navy);text-decoration:none;line-height:30px;padding:0 14px;margin-right:9px}
.nav a.active{background:var(--gold);color:#fff}
.band{left:0;top:120px;width:1200px;height:267px;background:radial-gradient(ellipse at 75% 40%,var(--orange-light),var(--orange-band) 70%)}
.photo{left:186px;top:129px;width:543px;height:248px;border-radius:4px;background:linear-gradient(135deg,#c9d7dc,#8ea4b0 45%,#3b4650);overflow:hidden}
.photo .caption{position:absolute;left:0;bottom:0;width:100%;height:49px;background:rgba(40,40,40,.55);color:#f3c64a;font-size:17px;line-height:49px;padding-left:5px}
.arrow{width:27px;height:27px}
.testi h2{left:785px;top:133px;font-weight:400;font-size:27px;color:#5a2a05}
.testi p{left:790px;top:176px;width:226px;font-size:10px;line-height:16.6px;text-align:justify;color:#3a2405}
.quote{font-family:"Tinos",serif;font-size:44px;color:#c98712}
.btn-more{left:900px;top:348px;width:110px;height:20px;background:linear-gradient(#fff,#e3e3e3);border-radius:2px;font-size:12px;line-height:20px;text-align:center;color:#222}
.welcome h1{left:160px;top:402px;font-family:"Tinos",serif;font-weight:400;font-size:24px;color:#333}
.welcome p{left:164px;top:436px;width:880px;font-size:11.5px;line-height:17px;color:#333}
.boxes{left:159px;top:486px;width:884px;height:143px;display:flex}
.box{flex:1;position:relative;color:#fff;padding:10px 14px}
.box h3{font-family:"Tinos",serif;font-weight:400;font-size:23px}
.box p{font-size:10.5px;line-height:16.5px;margin-top:12px;width:266px;letter-spacing:.1px}
.box .read{position:absolute;left:17px;bottom:8px;background:#fff;color:#222;font-size:10px;padding:3px 9px}
.box svg{position:absolute;right:18px;top:12px}
.b1{background:var(--green)} .b2{background:var(--blue-box)} .b3{background:var(--red-box)}
.col h2{font-family:"Tinos",serif;font-weight:400;font-size:24px;color:#333;padding-bottom:4px;border-bottom:1px dotted var(--line)}
.services{left:160px;top:652px;width:195px}
.services ul{list-style:none;margin-top:14px}
.services li{font-size:12.5px;height:22px;display:flex;align-items:center;gap:8px;color:#222;white-space:nowrap}
.bullet{width:13px;height:13px;border-radius:50%;background:var(--gold);position:relative;flex:none}
.bullet::after{content:"";position:absolute;left:5px;top:3.5px;border-left:4px solid #fff;border-top:3px solid transparent;border-bottom:3px solid transparent}
.clients{left:406px;top:652px;width:196px}
.news{left:626px;top:652px;width:196px}
.list{margin-top:11px;margin-left:-12px}
.item{background:var(--panel);height:41px;margin-bottom:4px;position:relative;padding:5px 0 0 40px}
.item .t{font-size:13px;color:#333;white-space:nowrap}
.item .s{font-size:10px;color:var(--rust);margin-top:4px}
.item .ic{position:absolute;left:12px;top:6px;width:13px;height:13px;border-radius:50%;background:#999}
.news .item .ic{background:#6d8fb6}
.item .ic::after{content:"";position:absolute;left:5px;top:3.5px;border-left:4px solid #fff;border-top:3px solid transparent;border-bottom:3px solid transparent}
.signup{left:846px;top:652px;width:197px}
.field{width:198px;height:22px;border:1px solid #ccc;font-size:10px;color:#555;padding:5px 9px;margin-top:8px;background:#fff}
.field:first-of-type{margin-top:11px}
.submit{margin-top:10px;width:75px;height:21px;background:var(--gold);font-size:12px;line-height:21px;text-align:center;color:#222}
.connect{left:847px;top:794px;width:196px}
.social{display:flex;gap:7px;margin-top:10px}
.social span{width:28px;height:28px;border-radius:4px}
.footer{left:0;top:905px;width:1200px;height:94px;border-top:3px solid #e4e4e4;background:linear-gradient(#f0f0f0,#fff)}
.footer nav{position:absolute;left:161px;top:31px;display:flex;gap:12px;font-size:12px;color:#222}
.footer .copy{position:absolute;left:161px;top:52px;font-size:10.5px;color:#7a4a00}
.footer .brand{position:absolute;left:853px;top:30px}
</style>
</head>
<body>
<header class="abs header">
  <div class="abs brand">Pixel Harbor</div>
  <div class="abs phones">(P) 214.555.0184<br>(F) 214.555.0137</div>
</header>
<nav class="abs nav">
  <a class="active">Home</a><a>About us</a><a>Hostroy</a><a>Sales Team &amp; Partners</a><a>Clients</a><a>Services</a><a>Testimonials</a><a>Contact Us</a>
</nav>
<section class="abs band"></section>
<div class="abs photo" role="img" aria-label="Photo of a smiling business team in an office">
  <div class="caption">We Provide Quality Services in the Sphere of Business Opportunities</div>
</div>
<svg class="abs arrow" style="left:158px;top:234px" viewBox="0 0 27 27"><circle cx="13.5" cy="13.5" r="12.5" fill="#fff" stroke="#ccc"/><path d="M16 8 L9 13.5 L16 19Z" fill="#1a3f8f"/></svg>
<svg class="abs arrow" style="left:731px;top:235px" viewBox="0 0 27 27"><circle cx="13.5" cy="13.5" r="12.5" fill="#fff" stroke="#ccc"/><path d="M11 8 L18 13.5 L11 19Z" fill="#1a3f8f"/></svg>
<div class="testi">
  <h2 class="abs">Clients Testimonials</h2>
  <span class="abs quote" style="left:760px;top:160px">“</span>
  <p class="abs">"I would like to express our appreciation for the excellent work performed by Pixel Harbor Inc. They successfully handled our website revamp, new brochure and newsletter projects, on time and on budget. It has been a pleasure working with your staff. They have listened to our ideas, had a firm understanding of what we wanted to accom-plish, and made recommendations to help us achieve a successful end result."</p>
  <span class="abs quote" style="left:1006px;top:300px">”</span>
  <div class="abs btn-more">More Testimonials</div>
</div>
<section class="welcome">
  <h1 class="abs">Welcome to our site</h1>
  <p class="abs">Out mission is to apply our experience, creativity and energy to assemble and execute marketing solutions with maximum impact. Implemention of carefully designed plans is undertaken with strict regard to value and result always striving to exceed client expectations</p>
</section>
<section class="abs boxes">
  <div class="box b1"><h3>Who we are</h3>
    <svg width="46" height="26" viewBox="0 0 46 26"><path d="M6 9 H36 M30 3 L37 9 L30 15 M40 17 H10 M16 11 L9 17 L16 23" fill="none" stroke="#fff" stroke-width="4"/></svg>
    <p>Full service. Dynamic exposure. Negotiation savvy. More buying power. Expert placement. Comprehen-sive promotional opportunities. And big savings.</p><span class="read">Read More</span></div>
  <div class="box b2"><h3>Principle Profile</h3>
    <svg width="40" height="26" viewBox="0 0 40 26"><path d="M4 6 H14 A5 5 0 1 1 22 6 H32 V10 A5 5 0 1 1 32 18 V22 H4Z" fill="#fff"/></svg>
    <p>Dana has vast experience in the advertising and marketing field. She is passionate about helping companies succeed; driving traffic,</p><span class="read">Read More</span></div>
  <div class="box b3"><h3 style="margin-top:4px">24/7 Client Support</h3>
    <svg width="38" height="38" viewBox="0 0 38 38"><circle cx="19" cy="19" r="16" fill="none" stroke="#fff" stroke-width="4"/><circle cx="19" cy="19" r="8" fill="none" stroke="#fff" stroke-width="3"/></svg>
    <p style="margin-top:16px">Full service. Dynamic exposure. Negotiation savvy. More buying power. Expert placement. Comprehen-sive promotional opportunities.</p><span class="read">Read More</span></div>
</section>
<section class="abs col services"><h2>Our Services</h2>
  <ul>
    <li><span class="bullet"></span>Medical / Health Care</li>
    <li><span class="bullet"></span>Retail Industry</li>
    <li><span class="bullet"></span>Automotive Industry</li>
    <li><span class="bullet"></span>Entertainment Industry</li>
    <li><span class="bullet"></span>Primary Services</li>
    <li><span class="bullet"></span>Media Planning &amp; Buying</li>
    <li><span class="bullet"></span>Campaign monitoring and reporting</li>
    <li><span class="bullet"></span>Commercial Production: TV &amp; Radio</li>
  </ul>
</section>
<section class="abs col clients"><h2>Our Clients</h2>
  <div class="list">
    <div class="item"><span class="ic"></span><div class="t">Maple Lane Market</div><div class="s">Retail - Grocery Industry</div></div>
    <div class="item"><span class="ic"></span><div class="t">Willow Brook Commons</div><div class="s">Retail - Shopping Center Industry</div></div>
    <div class="item"><span class="ic"></span><div class="t">Ironwheel Motors of Dallas</div><div class="s">Automotive Industry</div></div>
    <div class="item"><span class="ic"></span><div class="t">Dallas Ironwheel Cycles</div><div class="s">Automotive Industry</div></div>
  </div>
</section>
<section class="abs col news"><h2>Latest News</h2>
  <div class="list">
    <div class="item"><span class="ic"></span><div class="t">Lorem Ipsum is simply</div><div class="s">Posted byl - admin</div></div>
    <div class="item"><span class="ic"></span><div class="t">Lorem Ipsum is simply</div><div class="s">Posted byl - admin</div></div>
    <div class="item"><span class="ic"></span><div class="t">Lorem Ipsum is simply</div><div class="s">Posted byl - admin</div></div>
    <div class="item"><span class="ic"></span><div class="t">Lorem Ipsum is simply</div><div class="s">Posted byl - admin</div></div>
  </div>
</section>
<section class="abs col signup"><h2>Newsletter Signup</h2>
  <div class="field">Name</div>
  <div class="field">Email</div>
  <div class="submit">Submit Now</div>
</section>
<section class="abs col connect"><h2>Stay Connect</h2>
  <div class="social">
    <span style="background:#3b5b98"></span><span style="background:#5cc4e4"></span><span style="background:#e8e8e8"></span><span style="background:#c4302b"></span><span style="background:#f08a1d"></span>
  </div>
</section>
<footer class="abs footer">
  <nav><span>Home</span><span>About us</span><span>Hostroy</span><span>Sales Team &amp; Partners</span><span>Clients</span><span>Services</span><span>Testimonials</span><span>Contact Us</span></nav>
  <div class="copy">Copyright @ 2011 All right reserved</div>
  <div class="brand">Pixel Harbor</div>
</footer>
</body>
</html>
```